3 Politically Incorrect Greeting Cards

I would like to see some clean, colorful, and modern designs for 3 "politically incorrect" greeting cards aimed at young, single, successful women. I would like them to say:

Card 1: " Congratulations on not marrying the wrong person"
Card 2: " Congratulations on buying a house without a husband"
Card 3: " Thank you for not forgetting about me now that you have a boyfriend"

My initial thought was to have a white background with simple black writing, but I think a colorful background with a white text box in the middle might be more appropriate. I can't imagine the cards having any images/icons on them, but I'm open to suggestions if you think it would improve on the design. You guys are likely more creative than I am.

I've included a couple pics of looks I like - but like I said - I'm open to suggestions and what I like may not be appropriate for these cards. All the cards can have a similar esthetic or theme (maybe the same fonts but different colors or different color florals in each) or they can be completely different.

Target Market(s)

Young, single, successful women mid-20s to mid 40's.

Font styles to use
Serif
Sans Serif
Other font styles liked:
• Watercolour lettering maybe

Colors

Designer to choose colors to be used in the design.

Requirements
Must have
• Clean, colorful, bright, professional looking. The right tone for the message.
• I think the message is bold so the writing and colors have to be as well. I have included examples of ideas I like.
Nice to have
• Images, illustrations, icons, maybe patterns or some decorative details. Something to make the card more interesting than just the words (like the blue background with black letters one I made). I like a bright pattern with a white box in the center with the text.
Should not have
• Special effects, galaxy pictures, ugly images, bland colors.

```html
<!DOCTYPE html>
<html lang="en">
<head>
<meta charset="utf-8">
<title>Greeting Card Set</title>
<link href="https://fonts.googleapis.com/css2?family=Jost:wght@400;500&display=swap" rel="stylesheet">
<style>
  :root {
    --backdrop: #8f8985;
    --card: #ffffff;
    --card-shade: #ececec;
    --ink: #2f2f2f;
    --accent-marrying: #ec1a7d;
    --accent-boyfriend: #14a99d;
    --accent-house: #f7941d;
  }
  html, body {
    margin: 0;
    padding: 0;
    width: 1200px;
    height: 914px;
    overflow: hidden;
    background: var(--backdrop);
  }
  .card-set {
    position: relative;
    width: 1200px;
    height: 914px;
  }
  .card {
    position: absolute;
    width: 450px;
    height: 321px;
    background: linear-gradient(160deg, var(--card) 0%, var(--card) 45%, var(--card-shade) 100%);
    box-shadow: 2px 3px 6px rgba(0,0,0,0.35);
    display: flex;
    align-items: center;
    justify-content: center;
    font-family: "Jost", "Futura", sans-serif;
    font-weight: 400;
    color: var(--ink);
    text-transform: uppercase;
  }
  .card--marrying { left: 113px; top: 140px; }
  .card--boyfriend { left: 664px; top: 140px; }
  .card--house { left: 387px; top: 526px; }

  .message { margin: 0; letter-spacing: -0.3px; }
  .card--marrying .message {
    font-size: 25.5px;
    line-height: 33px;
    text-align: left;
    transform: translate(4px, 0);
  }
  .card--boyfriend .message {
    font-size: 20.5px;
    line-height: 29px;
    text-align: center;
    transform: translate(6px, 6px);
  }
  .card--house .message {
    font-size: 23.5px;
    line-height: 34px;
    text-align: center;
    transform: translate(3px, 2px);
  }
  .accent { font-weight: 500; }
  .card--marrying .accent { color: var(--accent-marrying); }
  .card--boyfriend .accent { color: var(--accent-boyfriend); }
  .card--house .accent { color: var(--accent-house); }
</style>
</head>
<body>
<main class="card-set">
  <section class="card card--marrying">
    <p class="message">
      Congratulations<br>
      On <span class="accent">not marrying</span><br>
      The wrong person
    </p>
  </section>

  <section class="card card--boyfriend">
    <p class="message">
      Thank you for <span class="accent">not forgetting</span><br>
      About me now that<br>
      You have a boyfriend
    </p>
  </section>

  <section class="card card--house">
    <p class="message">
      Congratulations on<br>
      Buying a house<br>
      <span class="accent">without</span> a husband
    </p>
  </section>
</main>
</body>
</html>
```